Template for Tolvik Advisory PowerPoint

We would like to create a new template for PowerPoint based on our current logo and graphic design guidelines. The template should reflect our corporate identity and be easy to use to create different kind of PowerPoint presentations for different kind of customers. The current design guideline that are attached reflect the "old" look of the PPT design and is only to be seen as a reference.
Tolvik Advisory is a Management consulting company working within both public and private sector. We focus on strategic business development and work in close cooperation with the customer to make sure it is the customer that will become the hero, our work is to support and guide them to the top.
The design should reflect a modern company working in close cooperation with our customers to help them innovate and describe their future business model, and also help them to reach that goal!
Words and taglines that we use. Passion for the future. The power of the organisation. Power of thoughts. Inspiration. Engagement.
What we have in mind is a modern, clean and elegant design based on our current logo. Tolvik Advisory is a Swedish Company working primarily on the Swedish market so the template must be possible to translate to Swedish (however the design can be done in english and be translated later)

Reason: I would like to extend the deadline to receive some more alternatives!

Reason: I'm out travelling and would like to extend the timeline to be able to choose the right design for our template. /Henrik

Target Market(s)

Our target market is within both private and public sector. Our main focus is CxO level executives within our clients organisation.

Industry/Entity Type

Management Consulting

Font styles to use
Sans Serif

Colors

Designer to choose colors to be used in the design.

Requirements
Must have
• A PPT template that contains both slides for traditional text and graphic. We like to work a lot with graphical presentations and try to limit the text on our slides to a minimum.
Nice to have
• Slides for different chapters within the presentation. Slides for powerful one-liners. Title slides. Thank you slides at the end.
Should not have
• Massive text....

```html
<!DOCTYPE html>
<html lang="en">
<head>
<meta charset="utf-8">
<title>Tolvik Advisory – Presentation Template</title>
<link rel="stylesheet" href="https://fonts.googleapis.com/css2?family=Roboto:wght@300;400;500;700;900&display=swap">
<style>
:root{
  --red:#c4122f;
  --red-dark:#9e0e26;
  --dark:#2a2a2c;
  --dark-2:#3a3a3d;
  --purple:#6b1f5e;
  --green:#6f9a3b;
  --grey:#e7e7e8;
  --grey-mid:#b9b9bc;
  --ink:#333336;
  --white:#ffffff;
  --photo-a:linear-gradient(135deg,#a7a9ad,#4a4c51);
  --photo-b:linear-gradient(135deg,#cfc7bd,#6f675f);
  --photo-c:linear-gradient(135deg,#8d96a3,#2f3540);
}
*{box-sizing:border-box;margin:0;padding:0}
html,body{width:1200px;height:4800px;overflow:hidden;background:#f2f2f3}
body{font-family:"Roboto",Arial,sans-serif;color:var(--ink)}
.deck{width:1200px;height:4800px;padding:8px;display:grid;grid-template-columns:repeat(3,1fr);grid-template-rows:repeat(21,1fr);gap:8px}
.slide{position:relative;overflow:hidden;background:var(--white);box-shadow:0 1px 2px rgba(0,0,0,.15)}
.slide.red{background:var(--red);color:var(--white)}
.slide.dark{background:var(--dark);color:var(--white)}
.slide.purple{background:var(--purple);color:var(--white)}
.a{position:absolute}
.photo{position:absolute;background:var(--photo-a)}
.photo.warm{background:var(--photo-b)}
.photo.cool{background:var(--photo-c)}
.brand{position:absolute;display:flex;align-items:center;gap:4px;font-weight:500;font-size:9px;color:var(--ink);letter-spacing:.2px;white-space:nowrap}
.brand .dot{width:7px;height:7px;border-radius:50%;background:var(--red);flex:none}
.brand.light{color:var(--white)}
.brand.light .dot{background:var(--white)}
.brand.top{top:10px;right:12px}
.brand.big{font-size:26px;gap:10px}
.brand.big .dot{width:20px;height:20px}
.brand.mid{font-size:15px;gap:6px}
.brand.mid .dot{width:11px;height:11px}
.brand.sm{font-size:12px;gap:5px}
.brand.sm .dot{width:9px;height:9px}
.center-box{position:absolute;display:flex;align-items:center;justify-content:center}
.center-box .brand{position:static}
.title{position:absolute;top:11px;left:14px;font-size:11px;font-weight:500;color:var(--ink)}
.title::after{content:"";display:block;width:16px;height:2px;background:var(--red);margin-top:3px}
.foot{position:absolute;left:0;right:0;bottom:0;height:6px;background:var(--red)}
.foot::after{content:"";position:absolute;right:0;top:-2px;width:10px;height:10px;background:var(--dark)}
.h-big{font-size:19px;font-weight:700;line-height:1.1}
.h-mid{font-size:14px;font-weight:700;line-height:1.15}
.sub{font-size:7px;opacity:.85}
.txt{font-size:6px;line-height:1.45;color:#666}
.txt.light{color:rgba(255,255,255,.8)}
.pill{display:inline-block;font-size:6px;padding:3px 8px;border-radius:2px;background:var(--dark);color:var(--white)}
.pill.red{background:var(--red)}
.icon-c{position:absolute;width:18px;height:18px;border-radius:50%;background:var(--red)}
.icon-c.dark{background:var(--dark)}
.icon-c.purple{background:var(--purple)}
.icon-c.green{background:var(--green)}
.icon-c.line{background:none;border:1.5px solid var(--white)}
.bar{position:absolute;bottom:0;background:var(--red)}
.bar.dk{background:var(--dark)}
.bar.pu{background:var(--purple)}
.row-item{position:absolute;font-size:7px;font-weight:500;color:var(--ink);white-space:nowrap}
.row-item small{display:block;font-size:5.5px;font-weight:400;color:#777;margin-top:2px}
.quote{font-size:10px;font-style:italic;line-height:1.4}
</style>
</head>
<body>
<main class="deck">

<!-- Row 1 -->
<section class="slide">
  <div class="center-box" style="inset:0"><div class="brand big"><span class="dot"></span>Tolvik Advisory</div></div>
</section>
<section class="slide red">
  <div class="photo cool" style="inset:0;opacity:.25" role="img" aria-label="City skyline photograph"></div>
  <div class="center-box" style="left:0;right:0;top:50px;height:24px"><div class="brand light mid"><span class="dot"></span>Tolvik Advisory</div></div>
  <div class="a h-mid" style="left:0;right:0;top:92px;text-align:center">Your Title Goes Here</div>
  <div class="a sub" style="left:0;right:0;top:112px;text-align:center">Your Subtitle Goes Here</div>
  <div class="a" style="left:0;right:0;top:128px;text-align:center"><span class="pill">Company Name Here</span></div>
</section>
<section class="slide dark">
  <div class="photo" style="inset:0;opacity:.45" role="img" aria-label="Dark building facade photograph"></div>
  <div class="a h-mid" style="right:20px;top:16px">Your Title Goes Here</div>
  <div class="a sub" style="right:20px;top:34px">Your Subtitle Goes Here</div>
  <div class="a" style="left:0;right:0;bottom:0;height:62px;background:var(--white);clip-path:polygon(0 60%,100% 0,100% 100%,0 100%)"></div>
  <div class="a txt" style="left:14px;bottom:10px">www.yourwebsite.com</div>
  <div class="brand" style="right:14px;bottom:10px"><span class="dot"></span>Tolvik Advisory</div>
</section>

<!-- Row 2 -->
<section class="slide">
  <div class="photo cool" style="right:0;top:0;width:200px;height:220px;clip-path:polygon(30% 0,100% 0,100% 100%,0 100%)" role="img" aria-label="Keyboard close-up photograph"></div>
  <div class="a" style="right:180px;top:0;width:40px;height:220px;background:var(--red);clip-path:polygon(70% 0,100% 0,30% 100%,0 100%)"></div>
  <div class="brand" style="left:14px;top:20px"><span class="dot"></span>Tolvik Advisory</div>
  <div class="a h-mid" style="left:14px;top:72px;color:var(--ink)">Your Title Goes Here</div>
  <div class="a sub" style="left:14px;top:92px">Your Subtitle Goes Here</div>
  <div class="a" style="left:14px;top:106px"><span class="pill red">Company Name Here</span></div>
  <div class="a txt" style="left:14px;bottom:12px">www.yourwebsite.com</div>
</section>
<section class="slide dark">
  <div class="a" style="left:0;top:80px;width:200px;height:26px;background:var(--red)"></div>
  <div class="a" style="left:16px;top:86px;font-size:10px;font-weight:700">Your Title Goes Here</div>
  <div class="a" style="left:0;top:108px;width:170px;height:14px;background:var(--dark-2)"></div>
  <div class="a sub" style="left:16px;top:111px">Your Subtitle Goes Here</div>
  <div class="brand light sm" style="right:16px;top:86px"><span class="dot"></span>Tolvik Advisory</div>
</section>
<section class="slide red">
  <div class="a" style="right:-40px;top:-40px;width:200px;height:200px;border-radius:50%;background:var(--red-dark);opacity:.5"></div>
  <div class="a h-mid" style="right:20px;top:100px">This Is Your Divider Page</div>
  <div class="a sub" style="right:20px;top:120px">Your Subtitle Goes Here</div>
</section>

<!-- Row 3 -->
<section class="slide">
  <div class="photo cool" style="left:0;top:0;width:220px;height:220px" role="img" aria-label="City skyline photograph"></div>
  <div class="a" style="left:150px;top:0;width:239px;height:220px;background:var(--red)"></div>
  <div class="icon-c line" style="left:172px;top:40px"></div>
  <div class="icon-c line" style="left:206px;top:40px"></div>
  <div class="icon-c line" style="left:240px;top:40px"></div>
  <div class="a h-mid" style="left:172px;top:90px;color:#fff">Your Title<br>Goes Here</div>
  <div class="a txt light" style="left:172px;top:130px;width:150px">Short line of supporting text here.</div>
</section>
<section class="slide dark">
  <div class="photo warm" style="left:0;top:0;width:389px;height:220px;opacity:.55" role="img" aria-label="Person working on a laptop photograph"></div>
  <div class="a" style="left:200px;top:70px;width:100px;height:70px;background:var(--dark)"></div>
  <div class="a h-mid" style="left:210px;top:84px;font-size:13px">Passion for<br>the future</div>
</section>
<section class="slide">
  <div class="photo warm" style="inset:0" role="img" aria-label="Business meeting with papers photograph"></div>
  <div class="a" style="left:-30px;top:30px;width:150px;height:150px;border-radius:50%;background:var(--red);opacity:.93"></div>
  <div class="a h-mid" style="left:22px;top:86px;color:#fff;font-size:13px">Passion for<br>the future</div>
</section>

<!-- Row 4 -->
<section class="slide">
  <div class="title">Our Agenda</div><div class="brand top"><span class="dot"></span>Tolvik Advisory</div>
  <div class="row-item" style="left:20px;top:60px">01 Agenda Item<small>Short point</small></div>
  <div class="row-item" style="left:20px;top:100px">02 Agenda Item<small>Short point</small></div>
  <div class="row-item" style="left:140px;top:60px">03 Agenda Item<small>Short point</small></div>
  <div class="row-item" style="left:140px;top:100px">04 Agenda Item<small>Short point</small></div>
  <div class="row-item" style="left:260px;top:60px">05 Agenda Item<small>Short point</small></div>
  <div class="row-item" style="left:260px;top:100px">06 Agenda Item<small>Short point</small></div>
  <div class="foot"></div>
</section>
<section class="slide">
  <div class="title">Bullets Point 1 Level</div><div class="brand top"><span class="dot"></span>Tolvik Advisory</div>
  <div class="row-item" style="left:20px;top:60px">■ Your Text Here<small>Short line</small></div>
  <div class="row-item" style="left:20px;top:100px">■ Your Text Here<small>Short line</small></div>
  <div class="row-item" style="left:140px;top:60px">■ Your Text Here<small>Short line</small></div>
  <div class="row-item" style="left:140px;top:100px">■ Your Text Here<small>Short line</small></div>
  <div class="row-item" style="left:260px;top:60px">■ Your Text Here<small>Short line</small></div>
  <div class="row-item" style="left:260px;top:100px">■ Your Text Here<small>Short line</small></div>
  <div class="foot"></div>
</section>
<section class="slide">
  <div class="photo warm" style="left:194px;top:0;width:195px;height:220px" role="img" aria-label="Team meeting photograph"></div>
  <div class="photo" style="left:0;top:110px;width:194px;height:110px" role="img" aria-label="Office workspace photograph"></div>
  <div class="a" style="left:0;top:0;width:194px;height:110px;background:var(--red)"></div>
  <div class="a txt light" style="left:14px;top:20px;width:160px">Lorem ipsum dolor sit amet, consectetur adipiscing elit, sed do eiusmod tempor.</div>
  <div class="a" style="left:194px;top:110px;width:120px;height:110px;background:var(--purple)"></div>
  <div class="a txt light" style="left:204px;top:126px;width:100px">Short supporting text goes here.</div>
</section>

<!-- Row 5 -->
<section class="slide">
  <div class="title">Your Title Here</div><div class="brand top"><span class="dot"></span>Tolvik Advisory</div>
  <div class="a" style="left:0;top:50px;width:97px;height:130px;background:var(--dark)"></div>
  <div class="a" style="left:97px;top:50px;width:97px;height:130px;background:var(--red)"></div>
  <div class="a" style="left:194px;top:50px;width:97px;height:130px;background:var(--purple)"></div>
  <div class="a" style="left:291px;top:50px;width:98px;height:130px;background:var(--green)"></div>
  <div class="a txt light" style="left:10px;top:100px;width:80px">Your Text Here</div>
  <div class="a txt light" style="left:107px;top:100px;width:80px">Your Text Here</div>
  <div class="a txt light" style="left:204px;top:100px;width:80px">Your Text Here</div>
  <div class="a txt light" style="left:301px;top:100px;width:80px">Your Text Here</div>
  <div class="foot"></div>
</section>
<section class="slide">
  <div class="brand mid" style="left:150px;top:50px"><span class="dot"></span>Tolvik Advisory</div>
  <div class="a h-mid" style="left:150px;top:82px;font-size:12px">Divider Page</div>
  <div class="a sub" style="left:150px;top:100px">Your Subtitle Goes Here</div>
  <div class="a" style="left:0;right:0;bottom:0;height:40px;background:var(--red);clip-path:polygon(0 70%,100% 0,100% 100%,0 100%)"></div>
</section>
<section class="slide">
  <div class="title">Our Differences</div><div class="brand top"><span class="dot"></span>Tolvik Advisory</div>
  <div class="icon-c" style="left:20px;top:56px;width:12px;height:12px"></div><div class="row-item" style="left:38px;top:58px">Your Text Here</div>
  <div class="icon-c" style="left:20px;top:86px;width:12px;height:12px"></div><div class="row-item" style="left:38px;top:88px">Your Text Here</div>
  <div class="icon-c" style="left:20px;top:116px;width:12px;height:12px"></div><div class="row-item" style="left:38px;top:118px">Your Text Here</div>
  <div class="a" style="left:180px;top:50px;width:190px;height:90px;background:var(--dark)"></div>
  <div class="photo" style="left:190px;top:60px;width:170px;height:70px" role="img" aria-label="Laptop on desk photograph"></div>
  <div class="foot"></div>
</section>

<!-- Row 6 -->
<section class="slide">
  <div class="title">Text &amp; Bullet Area</div><div class="brand top"><span class="dot"></span>Tolvik Advisory</div>
  <div class="a txt" style="left:14px;top:50px;width:130px"><b style="color:var(--ink)">Heading Goes Here</b><br>Lorem ipsum dolor sit amet, consectetur adipiscing elit sed do.</div>
  <div class="icon-c" style="left:170px;top:54px;width:12px;height:12px"></div><div class="row-item" style="left:186px;top:56px">Your Text Here</div>
  <div class="icon-c dark" style="left:170px;top:80px;width:12px;height:12px"></div><div class="row-item" style="left:186px;top:82px">Your Text Here</div>
  <div class="icon-c purple" style="left:170px;top:106px;width:12px;height:12px"></div><div class="row-item" style="left:186px;top:108px">Your Text Here</div>
  <div class="icon-c green" style="left:170px;top:132px;width:12px;height:12px"></div><div class="row-item" style="left:186px;top:134px">Your Text Here</div>
  <div class="row-item" style="left:290px;top:56px">Your Text Here</div>
  <div class="row-item" style="left:290px;top:82px">Your Text Here</div>
  <div class="foot"></div>
</section>
<section class="slide dark">
  <div class="a" style="left:0;top:0;width:78px;height:220px;background:#333"></div>
  <div class="a" style="left:78px;top:0;width:78px;height:220px;background:#3e3e41"></div>
  <div class="a" style="left:156px;top:0;width:78px;height:220px;background:var(--red)"></div>
  <div class="a" style="left:234px;top:0;width:77px;height:220px;background:#333"></div>
  <div class="a" style="left:311px;top:0;width:78px;height:220px;background:#3e3e41"></div>
  <div class="icon-c line" style="left:30px;top:60px"></div><div class="icon-c line" style="left:108px;top:60px"></div><div class="icon-c line" style="left:186px;top:60px"></div><div class="icon-c line" style="left:264px;top:60px"></div><div class="icon-c line" style="left:341px;top:60px"></div>
  <div class="a txt light" style="left:12px;top:100px;width:60px">Heading Here</div>
  <div class="a txt light" style="left:90px;top:100px;width:60px">Heading Here</div>
  <div class="a txt light" style="left:168px;top:100px;width:60px">Heading Here</div>
  <div class="a txt light" style="left:246px;top:100px;width:60px">Heading Here</div>
  <div class="a txt light" style="left:323px;top:100px;width:60px">Heading Here</div>
</section>
<section class="slide">
  <div class="title">Our Mockup Area</div>
  <div class="a" style="left:110px;top:40px;width:170px;height:100px;background:var(--dark);border-radius:4px"></div>
  <div class="center-box" style="left:116px;top:46px;width:158px;height:88px;background:#fff"><div class="brand sm"><span class="dot"></span>Tolvik Advisory</div></div>
  <div class="a" style="left:95px;top:140px;width:200px;height:8px;background:#999;border-radius:0 0 4px 4px"></div>
  <div class="a" style="left:0;right:0;bottom:0;height:40px;background:var(--dark)"></div>
</section>

<!-- Row 7 -->
<section class="slide">
  <div class="photo" style="left:0;top:0;width:130px;height:220px;background:var(--dark)" role="img" aria-label="Picture placeholder"></div>
  <div class="a" style="left:30px;top:60px;width:70px;height:70px;border-radius:50%;background:#fff;display:flex;align-items:center;justify-content:center;font-size:8px;font-weight:700;text-align:center;color:var(--ink)">A<br>Picture<br>Slide</div>
  <div class="a" style="left:150px;top:40px;width:220px;height:90px">
    <div class="bar" style="left:0;width:12px;height:50%"></div><div class="bar pu" style="left:16px;width:12px;height:80%"></div>
    <div class="bar" style="left:50px;width:12px;height:65%"></div><div class="bar pu" style="left:66px;width:12px;height:40%"></div>
    <div class="bar" style="left:100px;width:12px;height:90%"></div><div class="bar pu" style="left:116px;width:12px;height:60%"></div>
    <div class="bar" style="left:150px;width:12px;height:70%"></div><div class="bar pu" style="left:166px;width:12px;height:95%"></div>
  </div>
  <div class="a" style="left:150px;top:150px;font-size:20px;font-weight:700;color:var(--purple)">85%</div>
  <div class="foot"></div>
</section>
<section class="slide dark">
  <div class="center-box" style="left:0;right:0;top:70px;height:40px"><div class="brand light big"><span class="dot"></span>Tolvik Advisory</div></div>
  <div class="a sub" style="left:0;right:0;top:118px;text-align:center">Your Subtitle Here</div>
</section>
<section class="slide">
  <div class="title">Our Mockup Area</div><div class="brand top"><span class="dot"></span>Tolvik Advisory</div>
  <div class="a txt" style="left:14px;top:50px;width:100px"><b style="color:var(--ink)">Heading Here</b><br>Short supporting text goes here for the mockup.</div>
  <div class="a" style="left:140px;top:40px;width:230px;height:130px;background:var(--dark);border-radius:4px"></div>
  <div class="center-box" style="left:146px;top:46px;width:218px;height:118px;background:#fff"><div class="brand mid" style="font-size:18px"><span class="dot" style="width:13px;height:13px"></span>Tolvik Advisory</div></div>
  <div class="a" style="left:235px;top:170px;width:40px;height:20px;background:#bbb"></div>
  <div class="foot"></div>
</section>

<!-- Row 8 -->
<section class="slide">
  <div class="a h-mid" style="left:14px;top:40px;font-size:12px">This Is Line<br>Chart Slide</div>
  <div class="a txt" style="left:14px;top:76px;width:90px">Short line of supporting chart text.</div>
  <svg class="a" style="left:130px;top:30px" width="240" height="140" viewBox="0 0 240 140">
    <line x1="0" y1="130" x2="240" y2="130" stroke="#ccc"/>
    <polyline points="10,40 80,100 150,60 230,20" fill="none" stroke="var(--red)" stroke-width="2"/>
    <polyline points="10,80 80,60 150,110 230,90" fill="none" stroke="var(--dark)" stroke-width="2"/>
  </svg>
  <div class="foot"></div>
</section>
<section class="slide red">
  <div class="photo warm" style="inset:0;opacity:.35" role="img" aria-label="Handshake photograph"></div>
  <div class="a" style="inset:0;background:linear-gradient(120deg,transparent 30%,rgba(196,18,47,.85) 30%)"></div>
  <div class="a h-mid" style="right:20px;top:100px">This Is Your Divider Page</div>
  <div class="a sub" style="right:20px;top:120px">Your Subtitle Goes Here</div>
</section>
<section class="slide">
  <div class="title">Your Title Goes Here</div><div class="brand top"><span class="dot"></span>Tolvik Advisory</div>
  <div class="photo" style="left:14px;top:44px;width:110px;height:60px" role="img" aria-label="Office photograph"></div>
  <div class="a" style="left:124px;top:44px;width:110px;height:60px;background:var(--red)"></div>
  <div class="a" style="left:132px;top:56px;font-size:8px;font-weight:700;color:#fff">Heading Goes Here</div>
  <div class="photo warm" style="left:250px;top:44px;width:120px;height:60px" role="img" aria-label="Meeting photograph"></div>
  <div class="a" style="left:14px;top:112px;width:110px;height:60px;background:var(--purple)"></div>
  <div class="a" style="left:22px;top:124px;font-size:8px;font-weight:700;color:#fff">Heading Goes Here</div>
  <div class="photo cool" style="left:124px;top:112px;width:110px;height:60px" role="img" aria-label="Laptop photograph"></div>
  <div class="a" style="left:250px;top:112px;width:120px;height:60px;background:var(--red)"></div>
  <div class="a" style="left:258px;top:124px;font-size:8px;font-weight:700;color:#fff">Heading Goes Here</div>
  <div class="foot"></div>
</section>

<!-- Row 9 -->
<section class="slide">
  <div class="photo warm" style="left:0;top:0;width:220px;height:220px" role="img" aria-label="Hands typing on laptop photograph"></div>
  <div class="a" style="left:210px;top:30px;width:179px;height:130px;background:var(--dark)"></div>
  <div class="a" style="left:224px;top:44px;font-size:11px;font-weight:500;color:#fff">About Us</div>
  <div class="a txt light" style="left:224px;top:64px;width:150px">Lorem ipsum dolor sit amet, consectetur adipiscing elit, sed do eiusmod tempor.</div>
</section>
<section class="slide dark">
  <div class="a" style="left:0;top:0;right:0;height:50px;background:#fff;clip-path:polygon(0 0,100% 0,100% 40%,0 100%)"></div>
  <div class="center-box" style="left:0;right:0;top:8px;height:20px"><div class="brand"><span class="dot"></span>Tolvik Advisory</div></div>
  <div class="a h-mid" style="left:0;right:0;top:100px;text-align:center">This Is Your Divider Page</div>
  <div class="a sub" style="left:0;right:0;top:120px;text-align:center">Your Subtitle Goes Here</div>
</section>
<section class="slide">
  <div class="title">Quote Area</div>
  <div class="photo cool" style="left:190px;top:0;width:199px;height:220px" role="img" aria-label="Person walking in a modern building photograph"></div>
  <div class="a" style="left:14px;top:50px;width:176px;height:120px;background:var(--dark)"></div>
  <div class="a quote" style="left:26px;top:64px;width:150px;color:#fff;font-size:8px">“Coming together is a beginning. Keeping together is progress. Working together is success.”</div>
  <div class="a txt light" style="left:26px;top:140px">— Ada Lindqvist</div>
  <div class="foot"></div>
</section>

<!-- Row 10 -->
<section class="slide">
  <div class="title">Brand Detailed</div><div class="brand top"><span class="dot"></span>Tolvik Advisory</div>
  <div class="photo warm" style="left:14px;top:44px;width:180px;height:130px" role="img" aria-label="Office desk photograph"></div>
  <div class="a" style="left:194px;top:44px;width:88px;height:65px;background:var(--red)"></div>
  <div class="a" style="left:282px;top:44px;width:88px;height:65px;background:var(--green)"></div>
  <div class="a" style="left:194px;top:109px;width:88px;height:65px;background:var(--dark)"></div>
  <div class="a" style="left:282px;top:109px;width:88px;height:65px;background:var(--purple)"></div>
  <div class="a txt light" style="left:200px;top:54px">Strategy</div><div class="a txt light" style="left:288px;top:54px">Growth</div>
  <div class="a txt light" style="left:200px;top:119px">Vision</div><div class="a txt light" style="left:288px;top:119px">Team</div>
  <div class="foot"></div>
</section>
<section class="slide">
  <div class="title">Product Philosophy</div><div class="brand top"><span class="dot"></span>Tolvik Advisory</div>
  <svg class="a" style="left:150px;top:50px" width="90" height="90" viewBox="0 0 90 90">
    <circle cx="45" cy="45" r="32" fill="none" stroke="var(--red)" stroke-width="18" stroke-dasharray="50 151"/>
    <circle cx="45" cy="45" r="32" fill="none" stroke="var(--dark)" stroke-width="18" stroke-dasharray="50 151" stroke-dashoffset="-50"/>
    <circle cx="45" cy="45" r="32" fill="none" stroke="var(--purple)" stroke-width="18" stroke-dasharray="50 151" stroke-dashoffset="-100"/>
    <circle cx="45" cy="45" r="32" fill="none" stroke="var(--green)" stroke-width="18" stroke-dasharray="51 151" stroke-dashoffset="-150"/>
  </svg>
  <div class="row-item" style="left:20px;top:60px">Ideas<small>Short text</small></div>
  <div class="row-item" style="left:20px;top:110px">Focus<small>Short text</small></div>
  <div class="row-item" style="left:270px;top:60px">Action<small>Short text</small></div>
  <div class="row-item" style="left:270px;top:110px">Results<small>Short text</small></div>
  <div class="foot"></div>
</section>
<section class="slide">
  <div class="photo cool" style="left:0;top:0;right:0;height:70px;opacity:.6" role="img" aria-label="City skyline photograph"></div>
  <div class="a" style="left:30px;top:50px;width:330px;height:110px">
    <div class="bar dk" style="left:10px;width:18px;height:60%"></div><div class="bar" style="left:32px;width:18px;height:45%"></div>
    <div class="bar dk" style="left:90px;width:18px;height:75%"></div><div class="bar" style="left:112px;width:18px;height:90%"></div>
    <div class="bar dk" style="left:170px;width:18px;height:40%"></div><div class="bar" style="left:192px;width:18px;height:65%"></div>
    <div class="bar dk" style="left:250px;width:18px;height:55%"></div><div class="bar" style="left:272px;width:18px;height:35%"></div>
  </div>
  <div class="a" style="left:0;right:0;bottom:0;height:40px;background:var(--purple)"></div>
</section>

<!-- Row 11 -->
<section class="slide">
  <div class="title">Trending In The World</div><div class="brand top"><span class="dot"></span>Tolvik Advisory</div>
  <div class="a" style="left:20px;top:50px;width:200px;height:110px;background:var(--grey);border-radius:40px" role="img" aria-label="World map"></div>
  <div class="a" style="left:50px;top:80px;width:36px;height:36px;border-radius:50%;background:var(--red);color:#fff;font-size:9px;font-weight:700;display:flex;align-items:center;justify-content:center">80%</div>
  <div class="a" style="left:130px;top:70px;width:36px;height:36px;border-radius:50%;background:var(--purple);color:#fff;font-size:9px;font-weight:700;display:flex;align-items:center;justify-content:center">45%</div>
  <div class="icon-c" style="left:240px;top:56px;width:12px;height:12px"></div><div class="row-item" style="left:258px;top:58px">Your Text Here</div>
  <div class="icon-c purple" style="left:240px;top:90px;width:12px;height:12px"></div><div class="row-item" style="left:258px;top:92px">Your Text Here</div>
  <div class="icon-c dark" style="left:240px;top:124px;width:12px;height:12px"></div><div class="row-item" style="left:258px;top:126px">Your Text Here</div>
  <div class="foot"></div>
</section>
<section class="slide purple">
  <div class="icon-c line" style="left:60px;top:96px;width:28px;height:28px"></div>
  <div class="a h-mid" style="left:100px;top:96px">This Is Your Divider Page</div>
  <div class="a sub" style="left:100px;top:116px">Your Subtitle Goes Here</div>
</section>
<section class="slide">
  <div class="title">Our Vision &amp; Mission</div><div class="brand top"><span class="dot"></span>Tolvik Advisory</div>
  <div class="a" style="left:14px;top:44px;width:180px;height:130px;background:var(--red)"></div>
  <div class="a" style="left:24px;top:56px;font-size:9px;font-weight:700;color:#fff">Our Vision</div>
  <div class="a txt light" style="left:24px;top:72px;width:160px">Go to the next level. Without a path to the peak, guide every client forward.</div>
  <div class="a" style="left:210px;top:56px;font-size:9px;font-weight:700;color:var(--ink)">Our Missions</div>
  <div class="row-item" style="left:210px;top:78px">■ Your Text Here</div>
  <div class="row-item" style="left:210px;top:100px">■ Your Text Here</div>
  <div class="row-item" style="left:210px;top:122px">■ Your Text Here</div>
  <div class="foot"></div>
</section>

<!-- Row 12 -->
<section class="slide">
  <div class="title">Our Services</div><div class="brand top"><span class="dot"></span>Tolvik Advisory</div>
  <div class="photo" style="left:14px;top:44px;width:160px;height:110px" role="img" aria-label="Man with laptop photograph"></div>
  <div class="a" style="left:14px;top:154px;width:160px;height:22px;background:var(--red)"></div>
  <div class="a" style="left:22px;top:160px;font-size:7px;color:#fff">Your Title Goes Here</div>
  <div class="icon-c" style="left:196px;top:54px;width:14px;height:14px"></div><div class="row-item" style="left:216px;top:54px">Service Number One<small>Short text</small></div>
  <div class="icon-c" style="left:196px;top:92px;width:14px;height:14px"></div><div class="row-item" style="left:216px;top:92px">Service Number Two<small>Short text</small></div>
  <div class="icon-c" style="left:196px;top:130px;width:14px;height:14px"></div><div class="row-item" style="left:216px;top:130px">Service Number Three<small>Short text</small></div>
  <div class="foot"></div>
</section>
<section class="slide">
  <div class="title">Three Column Description</div><div class="brand top"><span class="dot"></span>Tolvik Advisory</div>
  <div class="a txt" style="left:14px;top:44px;width:300px">This is a place for your header text. Insert your text here, just replace the text with your own text.</div>
  <div class="a txt" style="left:14px;top:90px;width:110px"><b style="color:var(--red)">Heading One</b><br>Short supporting text for column.</div>
  <div class="a txt" style="left:140px;top:90px;width:110px"><b style="color:var(--red)">Heading Two</b><br>Short supporting text for column.</div>
  <div class="a txt" style="left:266px;top:90px;width:110px"><b style="color:var(--red)">Heading Three</b><br>Short supporting text for column.</div>
  <div class="foot"></div>
</section>
<section class="slide">
  <div class="title">Our Team</div><div class="brand top"><span class="dot"></span>Tolvik Advisory</div>
  <div class="a" style="left:160px;top:44px;width:70px;height:70px;border-radius:50%;background:var(--photo-b)" role="img" aria-label="Team member portrait"></div>
  <div class="a" style="left:0;right:0;top:122px;text-align:center;font-size:8px;font-weight:700">Team Member Name</div>
  <div class="a txt" style="left:0;right:0;top:136px;text-align:center">Job Title</div>
  <div class="a" style="left:0;right:0;top:152px;text-align:center;font-size:8px;color:var(--red)">★★★★★</div>
  <div class="foot"></div>
</section>

<!-- Row 13 -->
<section class="slide red">
  <div class="photo warm" style="inset:0;opacity:.3" role="img" aria-label="Team at work photograph"></div>
  <div class="a" style="left:0;top:0;width:180px;height:220px;background:#fff;clip-path:polygon(0 0,100% 0,40% 100%,0 100%);opacity:.95"></div>
  <div class="brand" style="left:14px;top:14px"><span class="dot"></span>Tolvik Advisory</div>
  <div class="a h-mid" style="left:30px;top:96px;color:#fff;text-shadow:none">THIS IS YOUR DIVIDER PAGE</div>
</section>
<section class="slide">
  <div class="title">Monthly Subscription</div><div class="brand top"><span class="dot"></span>Tolvik Advisory</div>
  <div class="a" style="left:0;right:0;top:90px;height:90px;background:var(--dark)"></div>
  <div class="a" style="left:40px;top:48px;width:90px;height:130px;background:#fff;box-shadow:0 1px 4px rgba(0,0,0,.25)"><div style="background:var(--green);color:#fff;font-weight:700;font-size:12px;text-align:center;padding:6px 0">$300</div><div class="txt" style="padding:6px;text-align:center">Basic plan features</div></div>
  <div class="a" style="left:150px;top:40px;width:90px;height:140px;background:#fff;box-shadow:0 1px 4px rgba(0,0,0,.25)"><div style="background:var(--red);color:#fff;font-weight:700;font-size:12px;text-align:center;padding:8px 0">$900</div><div class="txt" style="padding:6px;text-align:center">Premium plan features</div></div>
  <div class="a" style="left:260px;top:48px;width:90px;height:130px;background:#fff;box-shadow:0 1px 4px rgba(0,0,0,.25)"><div style="background:var(--purple);color:#fff;font-weight:700;font-size:12px;text-align:center;padding:6px 0">$450</div><div class="txt" style="padding:6px;text-align:center">Standard plan features</div></div>
</section>
<section class="slide">
  <div class="title">Your Title Goes Here</div><div class="brand top"><span class="dot"></span>Tolvik Advisory</div>
  <svg class="a" style="left:14px;top:44px" width="361" height="140" viewBox="0 0 361 140">
    <rect x="0" y="0" width="361" height="14" fill="var(--dark)"/>
    <rect x="120" y="0" width="60" height="14" fill="var(--red)"/>
    <g fill="var(--grey)"><rect y="28" width="361" height="14"/><rect y="56" width="361" height="14"/><rect y="84" width="361" height="14"/><rect y="112" width="361" height="14"/></g>
  </svg>
  <div class="foot"></div>
</section>

<!-- Row 14 -->
<section class="slide">
  <div class="title">Our Team</div><div class="brand top"><span class="dot"></span>Tolvik Advisory</div>
  <div class="a" style="left:14px;top:48px;width:34px;height:34px;background:var(--photo-b)" role="img" aria-label="Team member portrait"></div><div class="row-item" style="left:54px;top:50px">Henrik Name<small>Job Title</small></div>
  <div class="a" style="left:14px;top:104px;width:34px;height:34px;background:var(--photo-a)" role="img" aria-label="Team member portrait"></div><div class="row-item" style="left:54px;top:106px">Member Name<small>Job Title</small></div>
  <div class="a" style="left:200px;top:48px;width:34px;height:34px;background:var(--photo-b)" role="img" aria-label="Team member portrait"></div><div class="row-item" style="left:240px;top:50px">Member Name<small>Job Title</small></div>
  <div class="a" style="left:200px;top:104px;width:34px;height:34px;background:var(--photo-a)" role="img" aria-label="Team member portrait"></div><div class="row-item" style="left:240px;top:106px">Member Name<small>Job Title</small></div>
  <div class="foot"></div>
</section>
<section class="slide">
  <div class="title">Customer Testimonials</div><div class="brand top"><span class="dot"></span>Tolvik Advisory</div>
  <div class="a" style="left:60px;top:40px;width:40px;height:40px;border-radius:50%;background:var(--photo-b)" role="img" aria-label="Customer portrait"></div>
  <div class="a txt" style="left:120px;top:48px;width:220px">“Short customer quote about working together goes here.”</div>
  <div class="a" style="left:0;right:0;bottom:0;height:100px;background:var(--dark)"></div>
  <div class="icon-c line" style="left:70px;top:140px"></div><div class="icon-c line" style="left:150px;top:140px"></div><div class="icon-c line" style="left:230px;top:140px"></div><div class="icon-c line" style="left:310px;top:140px"></div>
</section>
<section class="slide">
  <div class="title">Two Pictures Slide</div><div class="brand top"><span class="dot"></span>Tolvik Advisory</div>
  <div class="a txt" style="left:14px;top:50px;width:110px">Lorem ipsum dolor sit amet consectetur adipiscing elit.</div>
  <div class="photo warm" style="left:140px;top:44px;width:110px;height:130px" role="img" aria-label="Meeting photograph"></div>
  <div class="photo" style="left:260px;top:44px;width:110px;height:130px" role="img" aria-label="Desk with notes photograph"></div>
  <div class="foot"></div>
</section>

<!-- Row 15 -->
<section class="slide">
  <div class="title">Title And Image + Text</div>
  <div class="a txt" style="left:14px;top:50px;width:140px">Lorem ipsum dolor sit amet, consectetur adipiscing elit, sed do eiusmod tempor incididunt.</div>
  <div class="a" style="left:14px;top:110px;width:140px;height:40px;background:var(--dark)"></div>
  <div class="photo" style="left:170px;top:0;width:219px;height:130px" role="img" aria-label="Man in office photograph"></div>
  <div class="foot"></div>
</section>
<section class="slide">
  <div class="title">Sales Comparison</div><div class="brand top"><span class="dot"></span>Tolvik Advisory</div>
  <div class="a" style="left:30px;top:50px;width:140px;height:80px">
    <div class="bar" style="left:0;width:14px;height:60%"></div><div class="bar pu" style="left:20px;width:14px;height:90%"></div><div class="bar" style="left:50px;width:14px;height:40%"></div><div class="bar pu" style="left:70px;width:14px;height:70%"></div>
  </div>
  <div class="a" style="left:30px;top:140px;font-size:20px;font-weight:700;color:var(--purple)">45%</div>
  <div class="a" style="left:210px;top:50px;width:150px;height:80px">
    <div class="bar" style="left:0;width:14px;height:80%"></div><div class="bar pu" style="left:20px;width:14px;height:50%"></div><div class="bar" style="left:50px;width:14px;height:95%"></div><div class="bar pu" style="left:70px;width:14px;height:65%"></div>
  </div>
  <div class="a" style="left:210px;top:140px;font-size:20px;font-weight:700;color:var(--red)">68%</div>
  <div class="foot"></div>
</section>
<section class="slide dark">
  <div class="photo cool" style="inset:0 0 60px 0;opacity:.7" role="img" aria-label="Modern building photograph"></div>
  <div class="a" style="left:0;right:0;top:160px;height:60px;background:var(--purple)"></div>
  <div class="a" style="left:210px;top:20px;font-size:10px;font-weight:700">Your Title Goes Here</div>
  <div class="a" style="left:0;top:160px;width:194px;height:60px;background:var(--red)"></div>
</section>

<!-- Row 16 -->
<section class="slide">
  <div class="title">Your Title</div>
  <div class="photo warm" style="left:150px;top:0;width:239px;height:220px" role="img" aria-label="Laptop and coffee photograph"></div>
  <div class="a" style="left:0;right:0;bottom:0;height:90px;background:var(--dark)"></div>
  <div class="a txt light" style="left:14px;top:144px;width:120px"><b>Budget Plan</b><br>Short supporting text.</div>
  <div class="a txt light" style="left:200px;top:144px;width:120px"><b>Budget Plan</b><br>Short supporting text.</div>
</section>
<section class="slide dark">
  <div class="a" style="left:0;right:0;top:0;height:60px;background:#fff"></div>
  <div class="center-box" style="left:0;right:0;top:18px;height:24px"><div class="brand mid"><span class="dot"></span>Tolvik Advisory</div></div>
  <div class="a" style="left:0;right:0;top:70px;text-align:center;font-size:9px">This Is Your Timeline Page</div>
  <div class="a" style="left:130px;top:100px;width:130px;height:40px;background:#fff"></div>
  <div class="a txt" style="left:140px;top:108px;width:110px;text-align:center">Your Heading Here</div>
  <div class="a" style="left:194px;top:140px;width:2px;height:80px;background:var(--red)"></div>
  <div class="icon-c" style="left:186px;top:170px"></div>
</section>
<section class="slide">
  <div class="title">Your Title</div><div class="brand top"><span class="dot"></span>Tolvik Advisory</div>
  <div class="icon-c" style="left:14px;top:56px;width:12px;height:12px"></div><div class="row-item" style="left:32px;top:58px">Your Text</div>
  <div class="icon-c" style="left:14px;top:90px;width:12px;height:12px"></div><div class="row-item" style="left:32px;top:92px">Your Text</div>
  <div class="icon-c" style="left:14px;top:124px;width:12px;height:12px"></div><div class="row-item" style="left:32px;top:126px">Your Text</div>
  <div class="photo warm" style="left:130px;top:40px;width:250px;height:140px" role="img" aria-label="Laptop on desk photograph"></div>
  <div class="foot"></div>
</section>

<!-- Row 17 -->
<section class="slide">
  <div class="title">Who We Are?</div><div class="brand top"><span class="dot"></span>Tolvik Advisory</div>
  <div class="a" style="left:14px;top:44px;font-size:10px;font-weight:500;color:var(--red)">A Title About<br>Contents</div>
  <div class="a" style="left:14px;top:84px;font-size:10px;font-weight:500;color:var(--red)">A Title About<br>Contents</div>
  <div class="a" style="left:14px;top:124px;font-size:10px;font-weight:500;color:var(--red)">A Title About<br>Contents</div>
  <div class="a" style="left:160px;top:110px;width:120px;height:50px;background:var(--red)"></div>
  <div class="a txt" style="left:160px;top:50px;width:200px">Short description for who we are.</div>
  <div class="foot"></div>
</section>
<section class="slide">
  <div class="a" style="left:193px;top:0;width:2px;height:220px;background:var(--red)"></div>
  <div class="icon-c" style="left:186px;top:20px;width:16px;height:16px"></div>
  <div class="a txt" style="left:140px;top:24px">Your Year</div>
  <div class="a" style="left:210px;top:18px;font-size:18px;font-weight:700;color:var(--red)">85%</div>
  <div class="icon-c" style="left:186px;top:90px;width:16px;height:16px"></div>
  <div class="a" style="left:40px;top:84px;width:130px;height:40px;background:var(--red)"></div>
  <div class="a txt light" style="left:48px;top:92px">Your Title Here</div>
  <div class="icon-c" style="left:186px;top:160px;width:16px;height:16px"></div>
  <div class="a" style="left:210px;top:156px;font-size:18px;font-weight:700;color:var(--purple)">58%</div>
</section>
<section class="slide">
  <div class="title">Bullet &amp; Chart Area</div><div class="brand top"><span class="dot"></span>Tolvik Advisory</div>
  <svg class="a" style="left:40px;top:50px" width="120" height="120" viewBox="0 0 120 120">
    <circle cx="60" cy="60" r="30" fill="none" stroke="var(--dark)" stroke-width="60" stroke-dasharray="113 189"/>
    <circle cx="60" cy="60" r="30" fill="none" stroke="var(--red)" stroke-width="60" stroke-dasharray="28 189" stroke-dashoffset="-113"/>
    <circle cx="60" cy="60" r="30" fill="none" stroke="var(--purple)" stroke-width="60" stroke-dasharray="19 189" stroke-dashoffset="-141"/>
    <circle cx="60" cy="60" r="30" fill="none" stroke="var(--green)" stroke-width="60" stroke-dasharray="29 189" stroke-dashoffset="-160"/>
  </svg>
  <div class="a" style="left:14px;top:80px;font-size:8px;font-weight:700;color:var(--red)">15%</div>
  <div class="a" style="left:14px;top:120px;font-size:8px;font-weight:700;color:var(--red)">25%</div>
  <div class="a" style="left:168px;top:104px;font-size:8px;font-weight:700">60%</div>
  <div class="icon-c" style="left:220px;top:56px;width:12px;height:12px"></div><div class="row-item" style="left:238px;top:58px">Category One</div>
  <div class="icon-c dark" style="left:220px;top:84px;width:12px;height:12px"></div><div class="row-item" style="left:238px;top:86px">Category Two</div>
  <div class="icon-c purple" style="left:220px;top:112px;width:12px;height:12px"></div><div class="row-item" style="left:238px;top:114px">Category Three</div>
  <div class="icon-c green" style="left:220px;top:140px;width:12px;height:12px"></div><div class="row-item" style="left:238px;top:142px">Category Four</div>
  <div class="foot"></div>
</section>

<!-- Row 18 -->
<section class="slide">
  <div class="title">Bullet &amp; Chart Area</div><div class="brand top"><span class="dot"></span>Tolvik Advisory</div>
  <div class="a" style="left:14px;top:54px;width:140px;height:7px;background:var(--red)"></div><div class="a" style="left:14px;top:63px;width:100px;height:7px;background:var(--dark)"></div>
  <div class="a" style="left:14px;top:84px;width:110px;height:7px;background:var(--red)"></div><div class="a" style="left:14px;top:93px;width:150px;height:7px;background:var(--dark)"></div>
  <div class="a" style="left:14px;top:114px;width:160px;height:7px;background:var(--red)"></div><div class="a" style="left:14px;top:123px;width:80px;height:7px;background:var(--dark)"></div>
  <div class="a" style="left:14px;top:144px;width:90px;height:7px;background:var(--red)"></div><div class="a" style="left:14px;top:153px;width:130px;height:7px;background:var(--dark)"></div>
  <div class="icon-c" style="left:220px;top:56px;width:12px;height:12px"></div><div class="row-item" style="left:238px;top:58px">Category One</div>
  <div class="icon-c dark" style="left:220px;top:86px;width:12px;height:12px"></div><div class="row-item" style="left:238px;top:88px">Category Two</div>
  <div class="icon-c purple" style="left:220px;top:116px;width:12px;height:12px"></div><div class="row-item" style="left:238px;top:118px">Category Three</div>
  <div class="foot"></div>
</section>
<section class="slide">
  <div class="a" style="left:193px;top:0;width:2px;height:150px;background:var(--red)"></div>
  <div class="icon-c" style="left:186px;top:20px;width:16px;height:16px"></div>
  <div class="a" style="left:210px;top:18px;font-size:9px;font-weight:700">Your<br>Title Here</div>
  <div class="icon-c" style="left:186px;top:70px;width:16px;height:16px"></div>
  <div class="a txt" style="left:140px;top:74px">Your Year</div>
  <div class="icon-c" style="left:186px;top:120px;width:16px;height:16px"></div>
  <div class="a txt" style="left:210px;top:124px">Your Year</div>
  <div class="center-box" style="left:0;right:0;top:176px;height:24px"><div class="brand mid"><span class="dot"></span>Tolvik Advisory</div></div>
</section>
<section class="slide red">
  <div class="photo warm" style="inset:0;opacity:.35" role="img" aria-label="Team discussion photograph"></div>
  <div class="a" style="left:230px;top:0;width:159px;height:36px;background:#fff;clip-path:polygon(10% 0,100% 0,100% 100%,0 100%)"></div>
  <div class="brand" style="right:14px;top:13px"><span class="dot"></span>Tolvik Advisory</div>
  <div class="a h-mid" style="right:20px;top:100px">This Is Your Divider Page</div>
  <div class="a sub" style="right:20px;top:120px">Your Subtitle Goes Here</div>
</section>

<!-- Row 19 -->
<section class="slide">
  <div class="title">Bullet &amp; Chart Area</div><div class="brand top"><span class="dot"></span>Tolvik Advisory</div>
  <div class="icon-c" style="left:14px;top:56px;width:12px;height:12px"></div><div class="row-item" style="left:32px;top:58px">Your Text Here</div>
  <div class="icon-c purple" style="left:14px;top:90px;width:12px;height:12px"></div><div class="row-item" style="left:32px;top:92px">Your Text Here</div>
  <div class="icon-c dark" style="left:14px;top:124px;width:12px;height:12px"></div><div class="row-item" style="left:32px;top:126px">Your Text Here</div>
  <div class="a" style="left:190px;top:50px;width:180px;height:120px">
    <div class="bar" style="left:0;width:14px;height:50%"></div><div class="bar pu" style="left:18px;width:14px;height:80%"></div>
    <div class="bar" style="left:60px;width:14px;height:90%"></div><div class="bar pu" style="left:78px;width:14px;height:60%"></div>
    <div class="bar" style="left:120px;width:14px;height:70%"></div><div class="bar pu" style="left:138px;width:14px;height:45%"></div>
  </div>
  <div class="foot"></div>
</section>
<section class="slide">
  <div class="title">Three Steps</div><div class="brand top"><span class="dot"></span>Tolvik Advisory</div>
  <div class="icon-c" style="left:14px;top:56px;width:12px;height:12px"></div><div class="row-item" style="left:32px;top:58px">Sample Text</div>
  <div class="icon-c purple" style="left:14px;top:96px;width:12px;height:12px"></div><div class="row-item" style="left:32px;top:98px">Sample Text</div>
  <div class="icon-c dark" style="left:14px;top:136px;width:12px;height:12px"></div><div class="row-item" style="left:32px;top:138px">Sample Text</div>
  <svg class="a" style="left:180px;top:36px" width="200" height="150" viewBox="0 0 200 150">
    <circle cx="60" cy="45" r="32" fill="none" stroke="var(--dark)" stroke-width="14"/>
    <circle cx="120" cy="75" r="32" fill="none" stroke="var(--red)" stroke-width="14"/>
    <circle cx="60" cy="105" r="32" fill="none" stroke="var(--purple)" stroke-width="14"/>
  </svg>
  <div class="foot"></div>
</section>
<section class="slide">
  <div class="title">Project Timeline</div><div class="brand top"><span class="dot"></span>Tolvik Advisory</div>
  <svg class="a" style="left:14px;top:44px" width="361" height="140" viewBox="0 0 361 140">
    <rect width="361" height="12" fill="var(--dark)"/>
    <g fill="var(--grey)"><rect y="20" width="361" height="14"/><rect y="40" width="361" height="14"/><rect y="60" width="361" height="14"/><rect y="80" width="361" height="14"/><rect y="100" width="361" height="14"/><rect y="120" width="361" height="14"/></g>
    <rect x="90" y="22" width="80" height="10" fill="var(--red)"/>
    <rect x="140" y="42" width="90" height="10" fill="var(--green)"/>
    <rect x="200" y="62" width="70" height="10" fill="var(--purple)"/>
    <rect x="110" y="82" width="120" height="10" fill="var(--red)"/>
    <rect x="240" y="102" width="90" height="10" fill="var(--dark)"/>
    <rect x="170" y="122" width="100" height="10" fill="var(--green)"/>
  </svg>
  <div class="foot"></div>
</section>

<!-- Row 20 -->
<section class="slide">
  <div class="photo warm" style="left:0;top:0;width:180px;height:220px" role="img" aria-label="People at a desk photograph"></div>
  <div class="a" style="left:150px;top:20px;width:220px;height:180px;background:var(--dark)"></div>
  <div class="a" style="left:166px;top:34px;font-size:11px;font-weight:500;color:#fff">Key Points</div>
  <div class="a txt light" style="left:166px;top:58px;width:190px">■ Your key point text here<br><br>■ Your key point text here<br><br>■ Your key point text here<br><br>■ Your key point text here</div>
</section>
<section class="slide dark">
  <div class="photo" style="inset:0;opacity:.35" role="img" aria-label="Office building photograph"></div>
  <div class="a" style="left:0;right:0;bottom:0;height:30px;background:#fff"></div>
  <div class="a h-mid" style="left:0;right:0;top:92px;text-align:center">This Is Your Divider Page</div>
  <div class="a sub" style="left:0;right:0;top:112px;text-align:center">Your Subtitle Goes Here</div>
</section>
<section class="slide">
  <div class="title">Three Bullets Area</div><div class="brand top"><span class="dot"></span>Tolvik Advisory</div>
  <div class="photo warm" style="left:14px;top:44px;width:361px;height:80px" role="img" aria-label="Team meeting photograph"></div>
  <div class="icon-c" style="left:61px;top:114px"></div><div class="icon-c" style="left:186px;top:114px"></div><div class="icon-c" style="left:321px;top:114px"></div>
  <div class="a txt" style="left:20px;top:142px;width:100px;text-align:center">Your text here</div>
  <div class="a txt" style="left:145px;top:142px;width:100px;text-align:center">Your text here</div>
  <div class="a txt" style="left:280px;top:142px;width:100px;text-align:center">Your text here</div>
  <div class="foot"></div>
</section>

<!-- Row 21 -->
<section class="slide">
  <div class="title">Compare Product</div><div class="brand top"><span class="dot"></span>Tolvik Advisory</div>
  <div class="a" style="left:40px;top:44px;width:50px;height:100px;background:var(--dark);border-radius:8px"></div>
  <div class="a txt" style="left:96px;top:50px;width:80px"><b style="color:var(--red)">Data Analysis</b><br>Short text here.</div>
  <div class="a" style="left:200px;top:44px;width:50px;height:100px;background:var(--dark);border-radius:8px"></div>
  <div class="a txt" style="left:256px;top:50px;width:80px"><b style="color:var(--purple)">Data Analysis</b><br>Short text here.</div>
  <div class="foot"></div>
</section>
<section class="slide red">
  <div class="photo warm" style="inset:0;opacity:.3" role="img" aria-label="Business people photograph"></div>
  <div class="a" style="left:20px;top:84px;font-size:20px;font-weight:700">Thank You</div>
  <div class="a sub" style="left:20px;top:110px">Send Your Feedback</div>
  <div class="a" style="left:200px;top:30px;width:160px;height:160px;border-radius:50%;background:#fff;border:6px solid var(--dark)"></div>
</section>
<section class="slide red">
  <div class="a" style="left:-40px;top:40px;width:180px;height:180px;border-radius:50%;background:var(--red-dark);opacity:.6"></div>
  <div class="a" style="left:220px;top:-60px;width:220px;height:220px;border-radius:50%;background:var(--red-dark);opacity:.4"></div>
  <div class="a" style="left:0;right:0;top:98px;text-align:center;font-size:18px;font-weight:700">Thank You</div>
</section>

</main>
</body>
</html>
```